Business card design needed

My company specialises in carpentry and building services.
Based in Brisbane QLD
We also do:
property maintenance
plastering
painting
tiling
property maintenance

Industry/Entity Type

Carpentry

Contact Information for Business Card

Brand Name Co
Neil 0412555783
Derek 0493721068

```html
<!DOCTYPE html>
<html lang="en">
<head>
<meta charset="utf-8">
<title>Brand Name Co — Business Card</title>
<link rel="stylesheet" href="https://fonts.googleapis.com/css2?family=Open+Sans:wght@300;400&family=Arimo:wght@400&display=swap">
<style>
  :root {
    --bg-core: #232628;
    --bg-mid: #141617;
    --bg-edge: #050606;
    --ink-heading: #c9d0d0;
    --ink-services: #a8b1b3;
    --ink-name: #c4cbcc;
    --divider: rgba(0, 0, 0, 0.55);
    --divider-glow: rgba(255, 255, 255, 0.05);
  }
  * { margin: 0; padding: 0; box-sizing: border-box; }
  html, body {
    width: 1200px;
    height: 695px;
    overflow: hidden;
    background: var(--bg-edge);
  }
  .card {
    position: relative;
    width: 1200px;
    height: 695px;
    overflow: hidden;
    background:
      radial-gradient(ellipse 520px 360px at 600px 340px, var(--bg-core) 0%, var(--bg-mid) 55%, var(--bg-edge) 100%);
  }
  .card__divider {
    position: absolute;
    left: 642px;
    top: 205px;
    width: 2px;
    height: 305px;
    background: linear-gradient(to bottom, transparent, var(--divider) 25%, var(--divider) 75%, transparent);
    box-shadow: 2px 0 0 var(--divider-glow);
  }
  .tagline {
    position: absolute;
    right: 590px;
    top: 262px;
    text-align: right;
  }
  .tagline__heading {
    font-family: "Open Sans", sans-serif;
    font-weight: 300;
    font-size: 38px;
    letter-spacing: -2.2px;
    color: var(--ink-heading);
    line-height: 1;
    white-space: nowrap;
  }
  .services {
    list-style: none;
    margin-top: 14px;
    font-family: "Arimo", sans-serif;
    font-size: 22px;
    letter-spacing: 1.2px;
    line-height: 27px;
    color: var(--ink-services);
  }
  .brand-name {
    position: absolute;
    left: 676px;
    top: 318px;
    font-family: "Open Sans", sans-serif;
    font-weight: 300;
    font-size: 44px;
    letter-spacing: -1px;
    color: var(--ink-name);
    line-height: 1;
    white-space: nowrap;
  }
</style>
</head>
<body>
  <main class="card">
    <section class="tagline">
      <h1 class="tagline__heading">Carpentry &amp; Building Services</h1>
      <ul class="services">
        <li>Property Maintenance</li>
        <li>Plastering</li>
        <li>Painting</li>
        <li>Tiling</li>
      </ul>
    </section>
    <div class="card__divider" aria-hidden="true"></div>
    <p class="brand-name">Brand Name Co</p>
  </main>
</body>
</html>
```